Super elegant, crisp & clean Business card design required

We recently upgraded our branding - which is on our website - tavorelstudio.com

I would like a simple, yet elegant, clean business card design please.

The font of my logo is Cinzel - and because of the natural colour - it's best to have this on a black background.

I would like to have the back of the business card - with simply my logo.

PLEASE DO NOT SUBMIT A COMPLICATED / UNCLEAN DESIGN

Industry/Entity Type

Business

Contact Information for Business Card

Dalvik Ostrander Photography

Font styles to use
Other font styles liked:
• Cinzel

Requirements
Must have
• A backpage with nothing but my logo
• Simple design - stands out
Should not have
• Colour that dont align with my logo
• Over complicated '/ non symmetrical design

```html
<!DOCTYPE html>
<html lang="en">
<head>
<meta charset="UTF-8">
<title>Dalvik Ostrander Photography — Business Card</title>
<link href="https://fonts.googleapis.com/css2?family=Cinzel:wght@400&family=Roboto:ital,wght@1,300&display=swap" rel="stylesheet">
<style>
  :root {
    --page: #ffffff;
    --card: #171a1b;
    --gold: #706b40;
    --gold-soft: #58552f;
  }
  * { margin: 0; padding: 0; box-sizing: border-box; }
  html, body {
    width: 1052px;
    height: 1200px;
    overflow: hidden;
    background: var(--page);
  }
  .sheet {
    position: relative;
    width: 1052px;
    height: 1200px;
  }
  .card {
    position: absolute;
    left: 66px;
    width: 920px;
    height: 525px;
    background: var(--card);
  }
  .card--front { top: 62px; }
  .card--back { top: 622px; }

  .brand-mark {
    position: absolute;
    left: 50%;
    top: 150px;
    transform: translateX(-50%);
    display: block;
  }
  .brand-name {
    position: absolute;
    left: 0;
    right: 0;
    top: 345px;
    text-align: center;
    font-family: "Cinzel", serif;
    font-weight: 400;
    font-size: 46px;
    line-height: 1;
    letter-spacing: 0.5px;
    color: var(--gold);
  }
  .brand-tagline {
    position: absolute;
    left: 0;
    right: 0;
    top: 398px;
    text-align: center;
    font-family: "Cinzel", serif;
    font-weight: 400;
    font-size: 19px;
    line-height: 1;
    letter-spacing: 17px;
    padding-left: 17px;
    color: var(--gold);
  }

  .contact {
    position: absolute;
    left: 0;
    right: 0;
    text-align: center;
    font-family: "Roboto", sans-serif;
    font-style: italic;
    font-weight: 300;
    font-size: 24px;
    line-height: 1;
    letter-spacing: 3px;
    color: var(--gold-soft);
  }
  .contact--web { top: 224px; }
  .contact--phone { top: 271px; }
</style>
</head>
<body>
  <main class="sheet">
    <section class="card card--front" aria-label="Card front">
      <svg class="brand-mark" width="120" height="120" viewBox="0 0 120 120" aria-hidden="true">
        <circle cx="60" cy="60" r="56" fill="none" stroke="var(--gold)" stroke-width="2"/>
      </svg>
      <h1 class="brand-name">Dalvik Ostrander</h1>
      <p class="brand-tagline">PHOTOGRAPHY</p>
    </section>

    <section class="card card--back" aria-label="Card back">
      <p class="contact contact--web">www.tavorelstudio.com</p>
      <p class="contact contact--phone">07700900418</p>
    </section>
  </main>
</body>
</html>
```